Automotive Accessories Business Card

Design a business template that match our new logo design and our industry.

https://www.kelvorauto.com/

Target Market(s)

Aftermarket auto parts and accessories

Industry/Entity Type

automotive

Contact Information for Business Card

company logo

Font styles to use
Serif
Sans Serif

Colors
EB3D1F
EC4F4E
F09395
F8D3D4
FCEDEE

```html
<!DOCTYPE html>
<html lang="en">
<head>
<meta charset="utf-8">
<title>Kelvor Auto Business Card</title>
<link href="https://fonts.googleapis.com/css2?family=Roboto:wght@300;400;700&display=swap" rel="stylesheet">
<style>
  :root {
    --brand-red: #d81f28;
    --ink-dark: #434244;
    --text-grey: #4a4a4c;
    --paper: #ffffff;
    --backdrop: #2c2c2c;
  }
  * { margin: 0; padding: 0; box-sizing: border-box; }
  html, body { width: 1200px; height: 1200px; overflow: hidden; }
  body {
    background: var(--backdrop);
    font-family: "Roboto", Arial, sans-serif;
    position: relative;
  }
  .card {
    position: absolute;
    left: 239px;
    width: 722px;
    height: 412px;
    border-radius: 19px;
    overflow: hidden;
  }
  .card--front { top: 140px; background: var(--paper); }
  .card--back { top: 645px; background: var(--brand-red); }
  .card__shapes { position: absolute; inset: 0; }

  .brand {
    position: absolute;
    display: flex;
    align-items: center;
    gap: 12px;
    color: var(--paper);
    font-weight: 700;
    letter-spacing: 1px;
    white-space: nowrap;
  }
  .brand__mark { background: var(--paper); display: block; }
  .brand--front { right: 34px; top: 66px; font-size: 40px; }
  .brand--front .brand__mark { width: 28px; height: 28px; }
  .brand--back { left: 0; right: 0; top: 172px; justify-content: center; font-size: 64px; }
  .brand--back .brand__mark { width: 44px; height: 44px; }

  .holder { position: absolute; left: 25px; top: 164px; }
  .holder__name { color: var(--brand-red); font-weight: 700; font-size: 35px; line-height: 1.05; }
  .holder__title { color: var(--text-grey); font-weight: 400; font-size: 20px; line-height: 1.1; }

  .contact {
    position: absolute;
    display: flex;
    align-items: center;
    gap: 12px;
    color: var(--text-grey);
    font-weight: 300;
    font-size: 19.5px;
    line-height: 1.05;
    white-space: nowrap;
  }
  .contact__icon {
    width: 37px; height: 38px;
    background: var(--brand-red);
    border-radius: 2px;
    flex: none;
    display: flex; align-items: center; justify-content: center;
  }
  .contact--phone { left: 25px; top: 267px; }
  .contact--address { left: 25px; top: 325px; }
  .contact--email { left: 373px; top: 267px; }
  .contact--web { left: 373px; top: 325px; }
</style>
</head>
<body>

<section class="card card--front" aria-label="Business card front">
  <svg class="card__shapes" viewBox="0 0 722 412" width="722" height="412">
    <polygon points="0,0 722,0 722,201 373,201 323,136 0,136" fill="var(--brand-red)"/>
    <polygon points="0,136 323,136 373,201 722,201 722,213 366,213 315,149 0,149" fill="var(--ink-dark)"/>
    <rect x="0" y="389" width="333" height="23" fill="var(--brand-red)" role="img" aria-label="Checkered racing flag strip"/>
    <rect x="333" y="389" width="389" height="23" fill="var(--ink-dark)"/>
  </svg>

  <div class="brand brand--front"><span class="brand__mark"></span>KELVOR AUTO</div>

  <div class="holder">
    <div class="holder__name">DANIEL REYES</div>
    <div class="holder__title">Designation</div>
  </div>

  <div class="contact contact--phone">
    <span class="contact__icon">
      <svg width="20" height="20" viewBox="0 0 24 24"><path fill="#fff" d="M6.6 10.8c1.4 2.8 3.8 5.1 6.6 6.6l2.2-2.2c.3-.3.7-.4 1-.2 1.1.4 2.300.6 3.6.6.6 0 1 .4 1 1V20c0 .6-.4 1-1 1C10.6 21 3 13.4 3 4c0-.6.4-1 1-1h3.5c.6 0 1 .4 1 1 0 1.300.2 2.5.6 3.6.1.3 0 .7-.2 1l-2.3 2.2z"/></svg>
    </span>
    <span>1-800-555-0147</span>
  </div>

  <div class="contact contact--address">
    <span class="contact__icon">
      <svg width="18" height="22" viewBox="0 0 24 24"><path fill="#fff" d="M12 2C8.1 2 5 5.1 5 9c0 5.2 7 13 7 13s7-7.8 7-13c0-3.9-3.1-7-7-7zm0 9.5a2.5 2.5 0 1 1 0-5 2.5 2.5 0 0 1 0 5z"/></svg>
    </span>
    <span>240 W. Oak St. Unit B, Fontana,<br>CA, 92335, United States</span>
  </div>

  <div class="contact contact--email">
    <span class="contact__icon">
      <svg width="24" height="18" viewBox="0 0 24 18"><rect x="1.5" y="1.5" width="21" height="15" fill="none" stroke="#fff" stroke-width="2"/><polyline points="2,2 12,10 22,2" fill="none" stroke="#fff" stroke-width="2"/></svg>
    </span>
    <span>sales@kelvorauto.com</span>
  </div>

  <div class="contact contact--web">
    <span class="contact__icon">
      <svg width="24" height="24" viewBox="0 0 24 24" fill="none" stroke="#fff" stroke-width="1.8"><circle cx="12" cy="12" r="10"/><ellipse cx="12" cy="12" rx="4.5" ry="10"/><line x1="2" y1="12" x2="22" y2="12"/><path d="M4 6.5h16M4 17.5h16"/></svg>
    </span>
    <span>kelvorauto.com</span>
  </div>
</section>

<section class="card card--back" aria-label="Business card back">
  <svg class="card__shapes" viewBox="0 0 722 412" width="722" height="412">
    <rect x="0" y="389" width="333" height="23" fill="#eb8f92" role="img" aria-label="Checkered racing flag strip"/>
    <rect x="333" y="389" width="389" height="23" fill="var(--paper)"/>
  </svg>
  <div class="brand brand--back"><span class="brand__mark"></span>KELVOR AUTO</div>
</section>

</body>
</html>
```